Professional Photography Business cards

I need business cards that include my logo which I have uploaded. I run a photography business. I am open to ideas but I would like one side to have my logo and the other side to have my contact info. I don't have a website made but I do own a website domain. I have uploaded 2 different logo color schemes. My business colors are Blue, black , and white.

Business Name
Business Phone Number
Business Email
Business Website address
Instagram

Industry/Entity Type

Professional Photography

Contact Information for Business Card

Phone Number: 555-314-8027 email: info@tkellan-studios.example Instagram: @t.kellanstudios website doman- www.tkellan-studios.example

Requirements
Must have
• I like the idea of a business card with a full black background front and back of card. My colors must include royal blue, black, and white

```html
<!DOCTYPE html>
<html lang="en">
<head>
<meta charset="UTF-8">
<title>T. Kellan Studios – Business Cards</title>
<link href="https://fonts.googleapis.com/css2?family=Roboto:wght@400;700&display=swap" rel="stylesheet">
<style>
  :root {
    --royal-blue: #2a2e8e;
    --white: #ffffff;
    --ink: #111111;
    --backdrop: #e8e9ec;
    --card-shadow: rgba(20, 22, 60, 0.2);
  }
  * { margin: 0; padding: 0; box-sizing: border-box; }
  html, body {
    width: 1200px;
    height: 800px;
    overflow: hidden;
  }
  body {
    background: var(--backdrop);
    font-family: "Roboto", Arial, sans-serif;
    display: flex;
    align-items: center;
    justify-content: center;
    gap: 48px;
  }
  .card {
    width: 540px;
    height: 309px;
    border-radius: 4px;
    overflow: hidden;
    box-shadow: 0 10px 28px var(--card-shadow);
    position: relative;
  }

  /* Front: brand on full black */
  .card-front {
    background: var(--ink);
    display: flex;
    align-items: center;
    justify-content: center;
    border-bottom: 10px solid var(--royal-blue);
  }
  .brand {
    display: flex;
    align-items: center;
    gap: 14px;
    font-weight: 400;
    font-size: 34px;
    letter-spacing: 0.5px;
    white-space: nowrap;
  }
  .brand-dot {
    width: 22px;
    height: 22px;
    border-radius: 50%;
    flex-shrink: 0;
  }
  .card-front .brand { color: var(--white); }
  .card-front .brand-dot { background: var(--royal-blue); }

  /* Back: white brand panel + blue contact panel */
  .card-back { display: flex; background: var(--ink); }
  .logo-panel {
    flex: 0 0 50%;
    background: var(--white);
    display: flex;
    align-items: center;
    justify-content: center;
  }
  .logo-panel .brand {
    color: var(--ink);
    font-size: 22px;
    gap: 10px;
  }
  .logo-panel .brand-dot {
    background: var(--royal-blue);
    width: 14px;
    height: 14px;
  }
  .contact-panel {
    flex: 1;
    background: var(--royal-blue);
    color: var(--white);
    padding: 38px 20px 0 30px;
    font-size: 13px;
    line-height: 1.6;
  }
  .contact-name {
    font-weight: 700;
    font-size: 17px;
    letter-spacing: 0.6px;
    text-transform: uppercase;
  }
  .contact-title { margin-bottom: 2px; }
  .contact-line {
    display: flex;
    align-items: center;
    gap: 7px;
    white-space: nowrap;
  }
  .contact-line svg {
    width: 11px;
    height: 11px;
    flex-shrink: 0;
  }
</style>
</head>
<body>

  <section class="card card-front" aria-label="Business card front">
    <div class="brand">
      <span class="brand-dot"></span>
      <span class="brand-name">T. Kellan Studios</span>
    </div>
  </section>

  <section class="card card-back" aria-label="Business card back">
    <div class="logo-panel">
      <div class="brand">
        <span class="brand-dot"></span>
        <span class="brand-name">T. Kellan Studios</span>
      </div>
    </div>
    <div class="contact-panel">
      <p class="contact-name">Tessa Kellan</p>
      <p class="contact-title">Photographer</p>
      <p>412 Linden Court Way</p>
      <p>Maple Falls, Oh 45000</p>
      <p class="contact-line">
        <svg viewBox="0 0 12 12" aria-hidden="true"><path fill="#fff" d="M2.5 1h2l1 2.8-1.3.9a6.5 6.5 0 0 0 3.1 3.1l.9-1.3 2.8 1v2A1.5 1.5 0 0 1 9.5 11 8.5 8.5 0 0 1 1 2.5 1.5 1.5 0 0 1 2.5 1z"/></svg>
        555-314-8027
      </p>
      <p class="contact-line">
        <svg viewBox="0 0 12 12" aria-hidden="true"><rect x="0.5" y="2" width="11" height="8" rx="1" fill="#fff"/><path d="M1 2.8 6 6.6l5-3.8" fill="none" stroke="#2a2e8e" stroke-width="1"/></svg>
        info@tkellan-studios.example
      </p>
      <p class="contact-line">
        <svg viewBox="0 0 12 12" aria-hidden="true"><circle cx="6" cy="6" r="5" fill="#fff"/></svg>
        @t.kellanstudios
      </p>
      <p class="contact-line">
        <svg viewBox="0 0 12 12" aria-hidden="true"><circle cx="6" cy="6" r="5.3" fill="none" stroke="#fff" stroke-width="1.2"/><ellipse cx="6" cy="6" rx="2.2" ry="5.3" fill="none" stroke="#fff" stroke-width="1"/><path d="M0.8 6h10.4" stroke="#fff" stroke-width="1"/></svg>
        www.tkellan-studios.example
      </p>
    </div>
  </section>

</body>
</html>
```